Infografiken für Anbieter von Sport-Trainingseinheiten
Zielgruppe
Wir unterstützen und motivieren Menschen regelmässig und Nachhaltig Bewegung und Sport in ihren Alltag zu integrieren. Dafür bieten wir individuelle Trainingseinheiten an, die ganzheitlich, abwechslungsreich sind und Spass machen.
Aufgabenstellung
4 einfache und einheitliche Infografiken im selben Stil für meine neue Webseite
Infografik 1: Was Personal Training ausmacht (Stichworte: motivierend, individuell, flexibel, ganzheitlich und abwechslungsreich)
Infografik 2: Ablauf/Prozess vom Erstgespräch über die Standortbestimmung, Zielsetzung, das Training bis zum Erfolg
Infografik 3: Zwei Säulen des Athletiktrainings: Verletzungsprävention und Leistungssteigerung (beide gleich wichtig)
Infografik 4: Der Prozess eines Athleten von der Ist-Soll-Analyse über Leistungstests, Trainingsplanung, Vorwettkampf bis zum Wettkampf (Weg Treppe - Ziel Trophäe)
Die Infografiken sollen sehr leicht lesbar, verständlich und vom Design her minimalisitisch sein. Eine schlichte, sportliche und elegante Darstellung ist erwünscht. Bei den Designelementen lasse ich mich überraschen. Ich bin offen für Vorschläge.
Farben: Schwarz, Weiss und Grau
Mir ist wichtig, dass die Grafiken denselben Stil haben und einheitlich erschienen.
Meine selbst erstellten Grafiken finden sie auf meiner 'noch' aktuellen Seite unter folgenden Links:
https://www.hb-fitcoaching.ch/personal-training/
https://www.hb-fitcoaching.ch/athletik-training/

```html
<!DOCTYPE html>
<html lang="de">
<head>
<meta charset="utf-8">
<title>Infografiken Personal Training und Athletiktraining</title>
<link href="https://fonts.googleapis.com/css2?family=Bodoni+Moda:opsz,wght@6..96,400;6..96,500&display=swap" rel="stylesheet">
<style>
  :root {
    --bg: #ffffff;
    --shape: #6b6b6f;
    --shape-dark: #3e3e42;
    --line: #444446;
    --thin-line: #8a8a8d;
    --text: #ffffff;
  }
  html, body {
    margin: 0;
    padding: 0;
    overflow: hidden;
    background: var(--bg);
  }
  .canvas {
    position: relative;
    width: 1200px;
    height: 848px;
    overflow: hidden;
    background: var(--bg);
    font-family: "Bodoni Moda", "Didot", serif;
    color: var(--text);
  }
  .shapes {
    position: absolute;
    inset: 0;
  }
  .pill {
    position: absolute;
    display: flex;
    align-items: center;
    justify-content: center;
    background: var(--shape);
    border-radius: 999px;
    color: var(--text);
    box-sizing: border-box;
  }
  /* Infografik 1 */
  .trait {
    left: 365px;
    width: 242px;
    height: 55px;
    font-size: 22px;
    letter-spacing: 1.2px;
  }
  .hub-title {
    position: absolute;
    left: 94px;
    top: 109px;
    width: 203px;
    height: 203px;
    border-radius: 50%;
    background: var(--shape);
    display: flex;
    align-items: center;
    justify-content: center;
    text-align: center;
    font-size: 29px;
    line-height: 1.3;
    letter-spacing: 1px;
    margin: 0;
    font-weight: 400;
  }
  /* Infografik 2 */
  .process-bar {
    position: absolute;
    left: 795px;
    top: 60px;
    width: 8px;
    height: 290px;
    background: var(--line);
  }
  .step {
    left: 768px;
    width: 290px;
    height: 56px;
    justify-content: flex-start;
    padding-left: 22px;
  }
  .step-number {
    width: 22px;
    text-align: center;
    font-size: 27px;
    font-weight: 500;
  }
  .step-label {
    flex: 1;
    text-align: center;
    font-size: 17px;
    letter-spacing: 1.2px;
    padding-right: 30px;
  }
  /* Infografik 4 */
  .stage {
    height: 65px;
    font-size: 14px;
    letter-spacing: 1.2px;
  }
  /* Infografik 3 */
  .venn-label {
    fill: var(--text);
    font-family: "Bodoni Moda", "Didot", serif;
    text-anchor: middle;
    letter-spacing: 1px;
  }
  .venn-label.pillar { font-size: 14px; }
  .venn-label.core { font-size: 21px; letter-spacing: 1.2px; }
</style>
</head>
<body>
<main class="canvas">

  <svg class="shapes" width="1200" height="848" viewBox="0 0 1200 848" aria-hidden="true">
    <defs>
      <clipPath id="upper-pillar">
        <circle cx="326" cy="571" r="122"/>
      </clipPath>
      <marker id="arrow-head" viewBox="0 0 10 10" refX="8" refY="5" markerWidth="9" markerHeight="9" orient="auto">
        <path d="M0 0 L10 5 L0 10 Z" fill="var(--line)"/>
      </marker>
    </defs>

    <!-- Infografik 1: connectors -->
    <g class="trait-connectors" stroke="var(--thin-line)" stroke-width="1.3">
      <line x1="196" y1="69" x2="365" y2="69"/>
      <line x1="314" y1="139" x2="365" y2="139"/>
      <line x1="335" y1="208" x2="365" y2="208"/>
      <line x1="314" y1="279" x2="365" y2="279"/>
      <line x1="196" y1="346" x2="365" y2="346"/>
    </g>
    <path class="trait-arc" d="M196 69 A139 139 0 0 1 196 346" fill="none" stroke="var(--shape-dark)" stroke-width="4"/>
    <g class="trait-dots" fill="var(--shape)">
      <circle cx="196" cy="69" r="11"/>
      <circle cx="314" cy="139" r="11"/>
      <circle cx="335" cy="208" r="11"/>
      <circle cx="314" cy="279" r="11"/>
      <circle cx="196" cy="346" r="11"/>
    </g>

    <!-- Infografik 3: two pillars -->
    <g class="pillars">
      <circle cx="326" cy="571" r="122" fill="var(--shape)"/>
      <circle cx="329" cy="698" r="122" fill="var(--shape)"/>
      <circle cx="329" cy="698" r="122" fill="var(--shape-dark)" clip-path="url(#upper-pillar)"/>
      <text class="venn-label pillar" x="327" y="549">VERLETZUNGSPRÄVENTION</text>
      <text class="venn-label pillar" x="332" y="727">LEISTUNGSSTEIGERUNG</text>
      <text class="venn-label core" x="327" y="625">ATHLETIK</text>
      <text class="venn-label core" x="327" y="654">TRAINING</text>
    </g>

    <!-- Infografik 4: progress arrow -->
    <line class="progress-arrow" x1="664" y1="809" x2="906" y2="443" stroke="var(--line)" stroke-width="1.5" marker-end="url(#arrow-head)"/>
  </svg>

  <!-- Infografik 1 -->
  <section class="traits">
    <h2 class="hub-title">PERSONAL<br>TRAINING</h2>
    <div class="pill trait" style="top:41px">individuell</div>
    <div class="pill trait" style="top:112px">motivierend</div>
    <div class="pill trait" style="top:182px">flexibel</div>
    <div class="pill trait" style="top:250px">ganzheitlich</div>
    <div class="pill trait" style="top:318px">abwechslungsreich</div>
  </section>

  <!-- Infografik 2 -->
  <section class="process">
    <div class="process-bar"></div>
    <div class="pill step" style="top:32px"><span class="step-number">1</span><span class="step-label">ERSTGESPRÄCH</span></div>
    <div class="pill step" style="top:103px"><span class="step-number">2</span><span class="step-label" style="font-size:15px;letter-spacing:0.8px;padding-right:0">STANDORTBESTIMMUNG</span></div>
    <div class="pill step" style="top:176px"><span class="step-number">3</span><span class="step-label">ZIELSETZUNG</span></div>
    <div class="pill step" style="top:248px"><span class="step-number">4</span><span class="step-label">TRAINING</span></div>
    <div class="pill step" style="top:324px"><span class="step-number">5</span><span class="step-label">ERFOLG</span></div>
  </section>

  <!-- Infografik 4 -->
  <section class="athlete-path">
    <div class="pill stage" style="left:907px;top:449px;width:123px">WETTKAMPF</div>
    <div class="pill stage" style="left:857px;top:524px;width:173px">VORWETTKAMPF</div>
    <div class="pill stage" style="left:807px;top:597px;width:223px">TRAININGSPLANUNG</div>
    <div class="pill stage" style="left:757px;top:672px;width:273px">LEISTUNGSTESTS</div>
    <div class="pill stage" style="left:709px;top:747px;width:321px">IST-SOLL-ANALYSE</div>
  </section>

</main>
</body>
</html>
```